Medical Research Web ad banners

We are a small independent Medical practice that conducts NRB pharmaceutical trials in Allergy, Asthma, and Rheumatology diseases. Our need is for 3 banner sizes to advertise for currently enrolling studies. Our Name is Quenby Research Center. We have a logo which I will attach (done through Pixel Huddle). We need the ad to say: Currently Enrolling Studies: (then list the following categories) Rheumatoid Arthritis, Asthma, Allergies, Lupus, COPD, Osteoarthritis. We do have a tag line which is: "Today's Question, Tomorrow's Answer" and a call to action statement: "Join Us in Finding the Answer" which can be used if you would like but we don't want to much "clutter" in the ads so they are easy to read and clicked on. The 3 sizes we are looking for are: Leader Board 728 x 90, Inline Rectangle 300 x 250, and Wide Skyscraper 160x 600.
Target Market(s)
Here is our website: www.quenbyresearch-example.com
We will be using these banners on Searchwick and TVK as well as some medical related sites to advertise for current studies. Our usual age audience is 18-85 year olds who have one of these diseases and are looking for a new or alternative treatment.
Industry/Entity Type
Pharmaceutical
Look and feel

```html
<!DOCTYPE html>
<html lang="en">
<head>
<meta charset="utf-8">
<title>Quenby Research Center – Enrolling Studies Banners</title>
<link rel="stylesheet" href="https://fonts.googleapis.com/css2?family=PT+Sans+Narrow:wght@400;700&display=swap">
<style>
  :root {
    --stage: #2b2b2b;
    --sky-top: #ffffff;
    --sky-mid: #d6ecfa;
    --sky-low: #7cc0ee;
    --sky-deep: #3f9be0;
    --heading-blue: #2467b3;
    --tag-navy: #0c3d84;
    --list-green: #3b8d12;
    --logo-ink: #1b1b1b;
    --button-fill: #f4f9fe;
    --button-edge: #9fcbed;
    --photo-warm: #e6cdb6;
    --photo-light: #f6ece2;
  }
  * { box-sizing: border-box; margin: 0; padding: 0; }
  html, body { width: 1200px; height: 1176px; overflow: hidden; }
  body {
    background: var(--stage);
    font-family: "PT Sans Narrow", "Arial Narrow", sans-serif;
    position: relative;
  }
  .banner {
    position: absolute;
    overflow: hidden;
    background:
      radial-gradient(ellipse 70% 30% at 60% 80%, rgba(255,255,255,0.45), rgba(255,255,255,0) 70%),
      linear-gradient(180deg, var(--sky-top) 0%, var(--sky-mid) 35%, var(--sky-low) 75%, var(--sky-deep) 100%);
    text-align: center;
  }
  .photo {
    position: absolute;
    background:
      radial-gradient(circle at 45% 45%, var(--photo-warm) 0%, var(--photo-light) 45%, rgba(255,255,255,0) 75%);
  }
  .logo {
    position: absolute;
    display: flex;
    align-items: center;
    gap: 5px;
    color: var(--logo-ink);
    font-weight: 700;
    font-size: 22px;
    line-height: 1;
  }
  .logo-dot {
    width: 14px; height: 14px;
    border-radius: 50%;
    background: var(--logo-ink);
  }
  .heading {
    position: absolute;
    color: var(--heading-blue);
    font-weight: 400;
    line-height: 1;
  }
  .study-list {
    position: absolute;
    color: var(--list-green);
    font-weight: 700;
    line-height: 1.08;
  }
  .tagline {
    position: absolute;
    color: var(--tag-navy);
    font-weight: 700;
    line-height: 1.05;
  }
  .cta {
    position: absolute;
    display: flex;
    align-items: center;
    justify-content: center;
    background: var(--button-fill);
    border: 2px solid var(--button-edge);
    border-radius: 12px;
    color: var(--tag-navy);
    font-weight: 700;
    line-height: 1.1;
    box-shadow: 0 1px 3px rgba(0,0,0,0.2);
  }

  /* Leader board 728 x 90 */
  .leaderboard { left: 43px; top: 60px; width: 1123px; height: 137px; }
  .leaderboard .photo { left: -20px; top: -30px; width: 340px; height: 200px; }
  .leaderboard .logo { left: 8px; top: 100px; font-size: 24px; }
  .leaderboard .heading { left: 290px; width: 690px; top: 10px; font-size: 40px; }
  .leaderboard .study-list { left: 290px; width: 690px; top: 58px; font-size: 21px; }
  .leaderboard .tagline { left: 290px; width: 690px; top: 84px; font-size: 40px; }
  .leaderboard .cta { left: 994px; top: 26px; width: 120px; height: 86px; font-size: 18px; }

  /* Wide skyscraper 160 x 600 */
  .skyscraper { left: 310px; top: 214px; width: 247px; height: 926px; }
  .skyscraper .photo { left: -20px; top: -20px; width: 287px; height: 270px; }
  .skyscraper .logo { left: 82px; top: 252px; }
  .skyscraper .heading { left: 0; width: 100%; top: 308px; font-size: 48px; line-height: 0.98; }
  .skyscraper .study-list { left: 0; width: 100%; top: 482px; font-size: 23px; }
  .skyscraper .tagline { left: 0; width: 100%; top: 614px; font-size: 40px; }
  .skyscraper .cta { left: 55px; top: 815px; width: 130px; height: 89px; font-size: 19px; }

  /* Inline rectangle 300 x 250 */
  .rectangle { left: 609px; top: 339px; width: 462px; height: 384px; }
  .rectangle .photo { left: -20px; top: -20px; width: 290px; height: 200px; }
  .rectangle .logo { left: 26px; top: 122px; }
  .rectangle .heading { left: 225px; width: 236px; top: 10px; font-size: 48px; line-height: 0.98; }
  .rectangle .study-list { left: 0; width: 100%; top: 170px; font-size: 23px; }
  .rectangle .tagline { left: 0; width: 100%; top: 236px; font-size: 40px; }
  .rectangle .cta { left: 65px; top: 341px; width: 321px; height: 39px; font-size: 21px; border-radius: 14px; }
</style>
</head>
<body>

<section class="banner leaderboard" aria-label="Leader board banner">
  <div class="photo" role="img" aria-label="Photo of a smiling family lying head to head, seen from above"></div>
  <div class="logo"><span class="logo-dot"></span>Quenby</div>
  <h2 class="heading">Currently Enrolling Studies</h2>
  <p class="study-list">Rheumatoid Arthritis, Asthma, Allergies, Lupus, COPD, Osteoarthritis</p>
  <p class="tagline">Today's Question, Tomorrow's Answer</p>
  <div class="cta">Join Us<br>in Finding<br>the Answer</div>
</section>

<section class="banner skyscraper" aria-label="Wide skyscraper banner">
  <div class="photo" role="img" aria-label="Photo of a smiling family lying head to head, seen from above"></div>
  <div class="logo"><span class="logo-dot"></span>Quenby</div>
  <h2 class="heading">Currently<br>Enrolling<br>Studies</h2>
  <p class="study-list">Rheumatoid Arthritis,<br>Asthma, Allergies,<br>Lupus, COPD,<br>Osteoarthritis</p>
  <p class="tagline">Today's<br>Question,<br>Tomorrow's<br>Answer</p>
  <div class="cta">Join Us<br>in Finding<br>the Answer</div>
</section>

<section class="banner rectangle" aria-label="Inline rectangle banner">
  <div class="photo" role="img" aria-label="Photo of a smiling family lying head to head, seen from above"></div>
  <div class="logo"><span class="logo-dot"></span>Quenby</div>
  <h2 class="heading">Currently<br>Enrolling<br>Studies</h2>
  <p class="study-list">Rheumatoid Arthritis, Asthma, Allergies,<br>Lupus, COPD, Osteoarthritis</p>
  <p class="tagline">Today's Question,<br>Tomorrow's Answer</p>
  <div class="cta">Join Us in Finding the Answer</div>
</section>

</body>
</html>
```